Harwell Construct, LLC Business Card
Business Car Design
Harwell Construct, LLC Business Card - Construction
Creative Brief
Professional
Tom Morrow
Owner
P.O. Box 5817 Larkmoor, SC 29990
tmorrow@harwellconstructsc.example
www.harwellconstructsc.example
Back of Business Card should be just the logo that fills up the page.

```html
<!DOCTYPE html>
<html lang="en">
<head>
<meta charset="utf-8">
<title>Harwell Construct, LLC Stationery</title>
<link href="https://fonts.googleapis.com/css2?family=Cinzel:wght@600&family=Open+Sans:wght@400;600&display=swap" rel="stylesheet">
<style>
  :root {
    --backdrop: #abadaf;
    --paper: #ffffff;
    --brown: #4a342c;
    --rule: #b9b9b9;
    --ink: #4d4d4d;
  }
  html, body { margin: 0; padding: 0; overflow: hidden; }
  .canvas {
    position: relative; width: 1200px; height: 626px; overflow: hidden;
    background: var(--backdrop);
    font-family: "Open Sans", Arial, sans-serif; color: var(--ink);
  }
  .sheet { position: absolute; background: var(--paper); overflow: hidden; box-shadow: 0 1px 3px rgba(0,0,0,.25); }
  .sheet svg.wave { position: absolute; left: 0; width: 100%; }
  .brand { position: absolute; text-align: center; color: var(--brown); font-family: "Cinzel", Georgia, serif; font-weight: 600; line-height: 1; }
  .brand .dot { display: block; margin: 0 auto 4px; border-radius: 50%; background: var(--brown); }
  .brand .name { display: block; letter-spacing: .04em; }
  .brand .sub { display: block; letter-spacing: .2em; margin-top: 2px; }

  .card { width: 180px; height: 101px; border-radius: 8px; }
  .card-front { left: 34px; top: 197px; }
  .card-front .brand { left: 0; right: 0; top: 22px; }
  .card-front .dot { width: 24px; height: 24px; }
  .card-front .name { font-size: 15px; }
  .card-front .sub { font-size: 5px; }

  .card-back { left: 34px; top: 312px; }
  .card-back .brand { left: 10px; top: 8px; width: 60px; }
  .card-back .dot { width: 12px; height: 12px; margin-bottom: 2px; }
  .card-back .name { font-size: 7px; }
  .card-back .sub { font-size: 3px; }
  .card-back .person { position: absolute; left: 14px; top: 56px; font-size: 5px; line-height: 1.3; }
  .card-back .person strong { display: block; font-weight: 600; color: var(--brown); font-size: 5.5px; }
  .card-back .contact { position: absolute; left: 92px; top: 54px; font-size: 3.6px; line-height: 1.45; }
  .card-back .wave { bottom: 0; height: 24px; }

  .letterhead { left: 230px; top: 29px; width: 435px; height: 564px; }
  .letterhead .brand { left: 0; right: 0; top: 28px; }
  .letterhead .dot { width: 28px; height: 28px; }
  .letterhead .name { font-size: 17px; }
  .letterhead .sub { font-size: 5px; }
  .footer-text { position: absolute; left: 0; right: 0; text-align: center; font-size: 4.2px; line-height: 1.5; }
  .letterhead .footer-text { top: 518px; }
  .letterhead .wave { bottom: 0; height: 52px; }

  .envelope-back { left: 679px; top: 79px; width: 487px; height: 209px; }
  .envelope-back .wave { top: 0; height: 90px; }

  .envelope-front { left: 679px; top: 336px; width: 487px; height: 211px; }
  .envelope-front .brand { left: 0; right: 0; top: 22px; }
  .envelope-front .dot { width: 26px; height: 26px; }
  .envelope-front .name { font-size: 15px; }
  .envelope-front .sub { font-size: 5px; }
  .envelope-front .footer-text { top: 172px; left: 140px; right: auto; width: 220px; }
  .envelope-front .wave { bottom: 0; height: 34px; }
</style>
</head>
<body>
<main class="canvas">

  <section class="sheet card card-front" aria-label="Business card front">
    <div class="brand"><span class="dot"></span><span class="name">HARWELL</span><span class="sub">CONSTRUCT, LLC</span></div>
  </section>

  <section class="sheet card card-back" aria-label="Business card back">
    <div class="brand"><span class="dot"></span><span class="name">HARWELL</span><span class="sub">CONSTRUCT, LLC</span></div>
    <div class="person"><strong>Tom Morrow</strong>Owner</div>
    <div class="contact">P.O. Box 5817<br>Larkmoor, SC 29990<br>tmorrow@harwellconstructsc.example<br>www.harwellconstructsc.example</div>
    <svg class="wave" viewBox="0 0 180 24" preserveAspectRatio="none" aria-hidden="true">
      <path d="M0 6 Q90 18 180 4" fill="none" stroke="var(--rule)" stroke-width="1.5"/>
      <path d="M0 10 Q90 22 180 8 L180 24 L0 24 Z" fill="var(--brown)"/>
    </svg>
  </section>

  <section class="sheet letterhead" aria-label="Letterhead">
    <div class="brand"><span class="dot"></span><span class="name">HARWELL</span><span class="sub">CONSTRUCT, LLC</span></div>
    <div class="footer-text">P.O. Box 5817 Larkmoor, SC 29990 | tmorrow@harwellconstructsc.example<br>www.harwellconstructsc.example</div>
    <svg class="wave" viewBox="0 0 435 52" preserveAspectRatio="none" aria-hidden="true">
      <path d="M0 18 Q220 38 435 10" fill="none" stroke="var(--rule)" stroke-width="3"/>
      <path d="M0 26 Q220 44 435 18 L435 52 L0 52 Z" fill="var(--brown)"/>
    </svg>
  </section>

  <section class="sheet envelope-back" aria-label="Envelope back">
    <svg class="wave" viewBox="0 0 487 90" preserveAspectRatio="none" aria-hidden="true">
      <path d="M0 0 L487 0 L487 74 Q250 56 0 78 Z" fill="var(--brown)"/>
      <path d="M0 84 Q250 62 487 80" fill="none" stroke="var(--rule)" stroke-width="2"/>
    </svg>
  </section>

  <section class="sheet envelope-front" aria-label="Envelope front">
    <div class="brand"><span class="dot"></span><span class="name">HARWELL</span><span class="sub">CONSTRUCT, LLC</span></div>
    <div class="footer-text">P.O. Box 5817 Larkmoor, SC 29990 | tmorrow@harwellconstructsc.example<br>www.harwellconstructsc.example</div>
    <svg class="wave" viewBox="0 0 487 34" preserveAspectRatio="none" aria-hidden="true">
      <path d="M0 8 Q250 26 487 2" fill="none" stroke="var(--rule)" stroke-width="2.5"/>
      <path d="M0 14 Q250 32 487 8 L487 34 L0 34 Z" fill="var(--brown)"/>
    </svg>
  </section>

</main>
</body>
</html>
```